Poster Design Project

Simple, very easy design project.

Design for a 20" x 30" poster (I will print the poster, you do the high-res design), of the attached.

(Pls note, this JPG is sideways and is an error). You are designing PORTRAIT

```html
<!DOCTYPE html>
<html lang="en">
<head>
<meta charset="utf-8">
<title>Great Ecommerce</title>
<link rel="stylesheet" href="https://fonts.googleapis.com/css2?family=Kaushan+Script&family=Open+Sans:wght@600;700&display=swap">
<style>
  :root {
    --teal: #178894;
    --teal-dark: #0b4f58;
    --teal-light: #5cc3cf;
    --ink: #2f2f2f;
    --paper: #ffffff;
    --steel-light: #d9dcdf;
    --steel-dark: #3a3d41;
    --globe-hot: #ffd23a;
    --globe-mid: #f05a1a;
    --globe-deep: #b3140c;
  }
  * { margin: 0; padding: 0; box-sizing: border-box; }
  html, body { width: 800px; height: 1200px; overflow: hidden; background: var(--paper); }
  .poster {
    position: relative;
    width: 800px;
    height: 1200px;
    background: var(--paper);
    overflow: hidden;
  }
  .top-band {
    position: absolute; left: 0; top: 0;
    width: 800px; height: 44px;
    background: var(--teal);
  }
  .title { position: absolute; left: 0; width: 800px; text-align: center; }
  .title-script {
    top: 70px;
    left: -12px;
    font-family: "Kaushan Script", cursive;
    font-size: 98px;
    color: #000;
    line-height: 1;
    letter-spacing: -2px;
  }
  .title-main {
    top: 170px;
    left: -10px;
    font-family: "Open Sans", sans-serif;
    font-weight: 700;
    font-size: 102px;
    color: var(--teal);
    line-height: 1;
    letter-spacing: -1px;
  }
  .values {
    position: absolute; left: 0; top: 0;
    list-style: none;
  }
  .value {
    position: absolute;
    left: 50px;
    height: 40px;
    display: flex;
    align-items: center;
    white-space: nowrap;
  }
  .value-globe {
    width: 36px; height: 36px;
    border-radius: 50%;
    background: radial-gradient(circle at 40% 35%, var(--globe-hot), var(--globe-mid) 55%, var(--globe-deep));
    flex: none;
  }
  .value-text {
    margin-left: 46px;
    font-family: "Open Sans", sans-serif;
    font-weight: 700;
    font-size: 37px;
    color: var(--ink);
  }
  .bottom-stripe {
    position: absolute; left: 0; top: 954px;
    width: 800px; height: 26px;
    background: var(--teal);
  }
  .bottom-art {
    position: absolute; left: 0; top: 980px;
    width: 800px; height: 220px;
    background:
      radial-gradient(ellipse at 78% 55%, var(--teal-light) 0%, var(--teal) 35%, var(--teal-dark) 75%),
      var(--teal-dark);
  }
  .at-sign-art {
    position: absolute; left: 100px; top: 892px;
    width: 262px; height: 308px;
    border-radius: 130px 130px 40px 40px;
    background: linear-gradient(160deg, var(--steel-light), #8b9096 45%, var(--steel-dark));
  }
</style>
</head>
<body>
<main class="poster">
  <div class="top-band"></div>

  <h1>
    <span class="title title-script">Great</span>
    <span class="title title-main">Ecommerce</span>
  </h1>

  <ul class="values">
    <li class="value" style="top:374px"><span class="value-globe" role="img" aria-label="Glowing globe bullet"></span><span class="value-text">Diversity of Thought</span></li>
    <li class="value" style="top:450px"><span class="value-globe" role="img" aria-label="Glowing globe bullet"></span><span class="value-text">Desire to Learn</span></li>
    <li class="value" style="top:526px"><span class="value-globe" role="img" aria-label="Glowing globe bullet"></span><span class="value-text">Never Settle</span></li>
    <li class="value" style="top:594px"><span class="value-globe" role="img" aria-label="Glowing globe bullet"></span><span class="value-text">Be a Problem Solver</span></li>
    <li class="value" style="top:668px"><span class="value-globe" role="img" aria-label="Glowing globe bullet"></span><span class="value-text" style="margin-left:50px">Work Fast (Web Speed)</span></li>
    <li class="value" style="top:740px"><span class="value-globe" role="img" aria-label="Glowing globe bullet"></span><span class="value-text" style="margin-left:48px">Execution - A Way of Life</span></li>
  </ul>

  <div class="bottom-stripe"></div>
  <div class="bottom-art" role="img" aria-label="Abstract teal digital swirl with hexagon pattern"></div>
  <div class="at-sign-art" role="img" aria-label="Chrome 3D at-sign symbol with cable"></div>
</main>
</body>
</html>
```